Quiet Harbor is a Counseling company and needs a website design.

I need a website design for my Counseling company based in Singapore. I provide counseling and other related services through therapy. I website is my front face and want it to represent my personality and the name of the company itself. My company represents non judgement, compassionate and a safe environment for people to come by and talk about their issues/problems.

I want the website to be something connected to nature earth like a perfect Sanctuary. When a person sees my website i want to immediately feel a piece of calmness and peace. This is essential to me.

Target Market(s)

All age groups above 13 years of age

Industry/Entity Type

It Company

Requirements
Must have
• Not too flashy and must connect to any common man irrespective of age
Should not have
• Good calm color concept

```html
<!DOCTYPE html>
<html lang="en">
<head>
<meta charset="utf-8">
<title>Quiet Harbor — About</title>
<link href="https://fonts.googleapis.com/css2?family=Delius&display=swap" rel="stylesheet">
<style>
  :root {
    --mist-top: #5d7189;
    --mist-mid: #7d93ad;
    --mist-low: #4f6378;
    --bar: rgba(38, 48, 62, 0.72);
    --band: rgba(34, 44, 58, 0.82);
    --menu: rgba(60, 70, 84, 0.92);
    --ink: #f4f6f8;
    --ink-soft: #d9dfe6;
    --track: rgba(90, 104, 122, 0.75);
    --thumb: rgba(120, 134, 152, 0.9);
    --arrow-box: #3f4b5a;
    --dot: #c9d1da;
    --dot-active: #2e3742;
  }
  * { margin: 0; padding: 0; box-sizing: border-box; }
  html, body { width: 1200px; height: 775px; overflow: hidden; }
  body {
    position: relative;
    font-family: "Delius", sans-serif;
    font-variant: small-caps;
    color: var(--ink);
    text-shadow: 1px 1px 2px rgba(0,0,0,0.75);
  }
  .scene-photo {
    position: absolute; inset: 0;
    background:
      radial-gradient(ellipse 60% 45% at 55% 25%, rgba(170,190,212,0.55), transparent 70%),
      linear-gradient(180deg, var(--mist-top) 0%, var(--mist-mid) 40%, var(--mist-low) 100%);
  }
  .top-bar {
    position: absolute; left: 0; top: 0; width: 1200px; height: 47px;
    background: var(--bar);
    border-bottom: 1px solid rgba(255,255,255,0.12);
  }
  .brand {
    position: absolute; left: 47px; top: 14px;
    font-size: 15px; letter-spacing: 0.5px;
  }
  .main-nav {
    position: absolute; right: 50px; top: 14px;
    font-size: 15px; letter-spacing: 0.5px;
    display: flex; gap: 7px;
  }
  .main-nav .sep { color: var(--ink-soft); }
  .main-nav .current { text-decoration: underline; text-underline-offset: 3px; }
  .submenu {
    position: absolute; left: 791px; top: 47px; width: 136px; height: 45px;
    background: var(--menu);
    padding: 5px 0 0 11px;
    font-size: 12px; line-height: 18px; letter-spacing: 0.5px;
  }
  .submenu .active { text-decoration: underline; }
  .about-panel {
    position: absolute; left: 629px; top: 130px; width: 490px;
  }
  .about-panel h1 {
    font-weight: 400; font-size: 29px; letter-spacing: 1px;
    margin-bottom: 20px;
  }
  .about-panel p {
    font-size: 15.5px; line-height: 25.9px; letter-spacing: 0.9px;
    text-indent: 18px; margin-bottom: 25.9px;
  }
  .scroll-track {
    position: absolute; left: 1118px; top: 134px; width: 16px; height: 478px;
    background: var(--track);
  }
  .scroll-thumb {
    position: absolute; left: 0; top: 28px; width: 16px; height: 96px;
    background: var(--thumb);
  }
  .scroll-btn {
    position: absolute; left: 0; width: 16px; height: 26px;
    background: var(--arrow-box);
  }
  .scroll-btn.up { top: 0; }
  .scroll-btn.down { bottom: 0; }
  .slide-dots {
    position: absolute; left: 936px; top: 694px;
    display: flex; gap: 11px;
  }
  .slide-dots span {
    width: 9px; height: 9px; border-radius: 50%;
    background: var(--dot);
  }
  .slide-dots span.on { background: var(--dot); box-shadow: inset 0 0 0 2px var(--dot); }
  .slide-dots span.on::after {
    content: ""; display: block; width: 5px; height: 5px; margin: 2px;
    border-radius: 50%; background: var(--dot-active);
  }
  .footer-band {
    position: absolute; left: 0; top: 728px; width: 1200px; height: 47px;
    background: var(--band);
    border-top: 1px solid rgba(255,255,255,0.1);
  }
</style>
</head>
<body>
  <div class="scene-photo" role="img" aria-label="Misty lakeside with swans flying past a small chapel and pine forest"></div>

  <header class="top-bar">
    <div class="brand">Quiet Harbor</div>
    <nav class="main-nav">
      <span>Home</span><span class="sep">/</span>
      <span class="current">About</span><span class="sep">/</span>
      <span>Consultation</span><span class="sep">/</span>
      <span>Resources</span><span class="sep">/</span>
      <span>Contact</span>
    </nav>
  </header>

  <div class="submenu">
    <div class="active">-About me</div>
    <div>-Quiet Harbor</div>
  </div>

  <section class="about-panel">
    <h1>About</h1>
    <p>Lorem ipsum dolor sit amet, consectetur adipiscing elit. Praesent ullamcorper interdum faucibus. Aenean vel tellus porta, luctus urna eu, ornare felis. Nulla accumsan, nisi in sodales faucibus, elit neque scelerisque sem, elementum interdum enim dui vitae justo. In commodo ipsum in vestibulum pretium. In non nisi enim. Ut laoreet sapien nisi, sed dapibus lectus porttitor vitae.</p>
    <p>Aliquam sagittis enim sodales, venenatis nibh ac, imperdiet justo. Nullam dolor nisi, viverra ac pretium sed, pulvinar eu neque. Curabitur mattis metus eros. Aenean faucibus, magna eget porttitor suscipit, mauris nisi semper lectus, dictum elementum metus elit vitae turpis. Nulla sed ante gravida, pharetra augue in, volutpat metus.</p>
  </section>

  <div class="scroll-track">
    <div class="scroll-btn up">
      <svg width="16" height="26" viewBox="0 0 16 26"><path d="M4 16 L8 10 L12 16 Z" fill="#e8ecf0"/></svg>
    </div>
    <div class="scroll-thumb"></div>
    <div class="scroll-btn down">
      <svg width="16" height="26" viewBox="0 0 16 26"><path d="M4 10 L8 16 L12 10 Z" fill="#e8ecf0"/></svg>
    </div>
  </div>

  <div class="slide-dots">
    <span class="on"></span><span></span><span></span><span></span><span></span>
  </div>

  <footer class="footer-band"></footer>
</body>
</html>
```